Brightfield Systems Business Cards

We need a new business card design for an Electrical company that also focuses on Audio Visual and Communications. We would like to see designs using our new company logo attached. The cards are for two different people outlined below. Full contact details will be provided when design winner is awarded, use generic information for now. Business card is to be double sided and we are open to layout and design ideas.

Target Market(s)

Residential & Commercial

Industry/Entity Type

Electrical

Contact Information for Business Card

Name: Corwin Blake - Senior Electrician, Name: Felix Wade - Technology Specialist.

Font styles to use
Sans Serif

Colors
0555a3
ffffff
000000

Requirements
Must have
• mobile number, email address, website address, PO Box address,
• A main heading somewhere on the card stating ELECTRICAL SERVICES - AUDIO VISUAL SALES & INSTALLATION - COMMUNICATIONS

```html
<!DOCTYPE html>
<html lang="en">
<head>
<meta charset="utf-8">
<title>Brightfield Systems – Business Card</title>
<link rel="stylesheet" href="https://fonts.googleapis.com/css2?family=League+Spartan:wght@700&family=Noto+Sans:wght@400&display=swap">
<style>
  :root {
    --brand-blue: #0a2b9c;
    --brand-blue-clear: rgba(10, 43, 156, 0);
    --card-white: #ffffff;
    --page-bg: #fbf9fb;
    --shadow: rgba(0, 0, 0, 0.45);
  }
  * { box-sizing: border-box; margin: 0; padding: 0; }
  html, body {
    width: 1200px; height: 840px; overflow: hidden;
    background: var(--page-bg);
  }
  .canvas { position: relative; width: 1200px; height: 840px; }

  .card {
    position: absolute; left: 276px; width: 629px; height: 368px;
    box-shadow: 3px 4px 6px var(--shadow);
  }

  /* Front */
  .card--front { top: 28px; background: var(--brand-blue); }
  .front-brand {
    position: absolute; left: 0; right: 0; top: 240px;
    display: flex; align-items: center; justify-content: center; gap: 14px;
    color: var(--card-white);
    font-family: "League Spartan", sans-serif; font-weight: 700;
    font-size: 40px; letter-spacing: 1px; text-transform: uppercase;
  }
  .front-brand__dot {
    width: 30px; height: 30px; border-radius: 50%; background: var(--card-white);
  }

  /* Back */
  .card--back { top: 414px; background: var(--card-white); overflow: hidden; }
  .services {
    position: absolute; top: 32px; left: 0; right: 30px; text-align: right;
    font-family: "Noto Sans", sans-serif; font-size: 14.2px; letter-spacing: 0.3px;
    color: var(--brand-blue); white-space: nowrap;
  }
  .paint-area {
    position: absolute; left: 0; top: 64px; width: 240px; height: 268px;
    background: linear-gradient(to right, var(--brand-blue) 0%, var(--brand-blue) 58%, var(--brand-blue-clear) 100%);
  }
  .back-brand {
    position: absolute; left: 34px; top: 166px; width: 92px; text-align: center;
    color: var(--card-white);
    font-family: "League Spartan", sans-serif; font-weight: 700;
    font-size: 12px; line-height: 1.15; letter-spacing: 0.5px; text-transform: uppercase;
  }
  .person { position: absolute; right: 43px; top: 68px; text-align: right; color: var(--brand-blue); }
  .person__name {
    font-family: "League Spartan", sans-serif; font-weight: 700;
    font-size: 37px; letter-spacing: 1.5px; line-height: 1;
  }
  .person__role {
    margin-top: 10px;
    font-family: "League Spartan", sans-serif; font-weight: 700;
    font-size: 13.5px; letter-spacing: 0.8px;
  }
  .contact {
    position: absolute; right: 42px; top: 202px; list-style: none; text-align: right;
    font-family: "Noto Sans", sans-serif; font-size: 13.8px; line-height: 24.5px;
    color: var(--brand-blue);
  }
  .contact__item { display: flex; justify-content: flex-end; align-items: center; gap: 5px; }
  .contact__icon { width: 14px; height: 14px; flex: none; }
</style>
</head>
<body>
<main class="canvas">

  <section class="card card--front" aria-label="Card front">
    <div class="front-brand"><span class="front-brand__dot"></span>Brightfield Systems</div>
  </section>

  <section class="card card--back" aria-label="Card back">
    <p class="services">ELECTRICAL SERVICES - AUDIO VISUAL SALES &amp; INSTALLATION - COMMUNICATIONS</p>

    <div class="paint-area" role="img" aria-label="Hand-painted blue brush-stroke wave running across the card"></div>
    <div class="back-brand">Brightfield<br>Systems</div>

    <div class="person">
      <h1 class="person__name">CORWIN BLAKE</h1>
      <p class="person__role">SENIOR ELECTRICIAN</p>
    </div>

    <ul class="contact">
      <li class="contact__item">123-456-7890
        <svg class="contact__icon" viewBox="0 0 16 16" aria-hidden="true"><path fill="var(--brand-blue)" d="M1 6 Q8 1 15 6 L13 8 L11 6 L5 6 L3 8 Z M4 8 H12 L14 14 H2 Z"/></svg></li>
      <li class="contact__item">corwin@brightfieldsystems.com
        <svg class="contact__icon" viewBox="0 0 16 16" aria-hidden="true"><text x="8" y="12.5" text-anchor="middle" font-family="Noto Sans, sans-serif" font-size="14" fill="var(--brand-blue)">@</text></svg></li>
      <li class="contact__item">www.brightfieldsystems.com
        <svg class="contact__icon" viewBox="0 0 16 16" aria-hidden="true"><circle cx="8" cy="8" r="6.5" fill="none" stroke="var(--brand-blue)" stroke-width="1.5"/><ellipse cx="8" cy="8" rx="2.8" ry="6.5" fill="none" stroke="var(--brand-blue)" stroke-width="1.2"/><line x1="1.5" y1="8" x2="14.5" y2="8" stroke="var(--brand-blue)" stroke-width="1.2"/></svg></li>
      <li class="contact__item">Streetname XX Po Box XXXX</li>
      <li class="contact__item">Citx Zipcode</li>
    </ul>
  </section>

</main>
</body>
</html>
```